Law Firm Advertising Design Needed

Law Office of Dorvel K Tansy provides legal services to businesses and individuals who have been or are being injured. Our main practice area is personal injury (car accidents, wrongful death, premises liability), but we are looking for an ad that highlights a lesser known area of our practice - insurance company bad faith and breach of contract.

This ad will be placed in 8 1/2" x 11" format in a local neighborhood directory. It will also be placed in a smaller format (to be determined) in the local newspaper of a region of Arizona that has recently lost a considerable number of homes and people to wildfire.

We want to convey through the ad that our firm is available to help if their insurance company is not paying a legitimate claim or not paying enough for their claim.

Because of the tragic nature of the events in Yarnell, we would like to avoid images of fire or anything resembling fire. However, the ad should capture the attention of individuals who are struggling through an insurance claim with all the stacks of paperwork and frustrated with unresponsive adjusters and unreasonably low offers.

The design should convey a feeling of safety, security and being taken care of.

Information that must be included in the ad are: the firm name (Law Office of Dorvel K Tansy), address (4857 W 17th Avenue, Ste 406, Phoenix, AZ 85033), the phone number (602-574-2930) and the fact that we have mobile offices available to assist in your area.

An example of text that has been used in the past is here:
"If your own insurance company is refusing to pay what you are owed on a claim, call the Law Office of Dorvel K Tansy. We fight for you by examining the reasons your insurance carrier is denying or making an insufficient offer on the claim; updating and correcting claim documentation; making a new demand and filing a lawsuit if necessary. Whether it's a simple misunderstanding or something more complicated, we can help!

Here are a few of the kinds of claims we handle:
- Hit and Run or Uninsured driver claims
- Fire, flood and property loss
- Life insurance benefits
- Health insurance claims
- Catastrophic losses
- Business insurance
- Wrongful Death Benefits

Our attorneys are available to help you cut through the nonsense. Call to make an appointment for a free consultation with an attorney today. "

An example of a previous ad for car accident services is attached for reference.
Updates

Hi Everyone,

The main lawyer involved in the decision making process has been giving me some feedback in general on the designs that I thought I would pass along.  He does not want the name of the law firm to be the first thing you notice when you look at the ad. Try to keep that small and possibly to the bottom of the ad. The phone number should be rather large, but the address should be rather small (we are required by the State Bar to include our address, but we don't want our location to limit the location of our clients because our mobile offices can travel to them).  He would prefer that the logo either not be included or be not a significant part of the ad.

                                   

Thanks!  I will continue providing individual feedback to ads received. 

Target Market(s)

Low to middle income residents of the State of Arizona with little or no college education

Industry/Entity Type

Insurance

```html
<!DOCTYPE html>
<html lang="en">
<head>
<meta charset="utf-8">
<title>We Fight For You – Law Office of Dorvel K Tansy</title>
<link rel="stylesheet" href="https://fonts.googleapis.com/css2?family=Cinzel:wght@700&family=Cormorant+Garamond:ital,wght@0,500;0,600;0,700;1,500;1,600;1,700&display=swap">
<style>
  :root {
    --page-bg: #ececec;
    --maroon: #6d2a55;
    --maroon-edge: #8a4a72;
    --navy: #172c4a;
    --ink-light: #f4f1f3;
    --tick: #8cc63f;
    --photo-light: #c9d9ea;
    --photo-mid: #8aa6c4;
    --photo-dark: #1e2c44;
  }
  * { box-sizing: border-box; margin: 0; padding: 0; }
  html, body { width: 1200px; height: 1000px; overflow: hidden; }
  body {
    background: var(--page-bg);
    font-family: "Cormorant Garamond", Georgia, serif;
    color: var(--ink-light);
    position: relative;
  }
  .flyer {
    position: absolute;
    left: 301px; top: 78px;
    width: 620px; height: 804px;
    background: var(--navy);
    box-shadow: 0 4px 14px rgba(0,0,0,0.25);
    display: flex; flex-direction: column;
  }
  .band {
    background: var(--maroon);
    border-top: 3px solid var(--maroon-edge);
    border-bottom: 3px solid var(--maroon-edge);
    text-align: center;
  }
  .headline {
    height: 72px;
    font-family: "Cinzel", "Times New Roman", serif;
    font-weight: 700;
    font-size: 55px;
    line-height: 64px;
    letter-spacing: 1px;
  }
  .intro {
    height: 264px;
    padding: 16px 24px 0;
  }
  .intro-text {
    font-size: 15.6px;
    font-weight: 500;
    line-height: 19.6px;
    text-align: justify;
  }
  .intro-text strong { font-weight: 700; }
  .availability {
    margin-top: 12px;
    font-size: 16px;
    font-style: italic;
    font-weight: 500;
  }
  .availability strong { font-weight: 700; letter-spacing: 0.5px; }
  .claims {
    margin-top: 8px;
    padding-left: 8px;
    display: grid;
    grid-template-columns: 335px 1fr;
    list-style: none;
    font-size: 15.6px;
    font-weight: 500;
    line-height: 18.4px;
  }
  .claims li { display: flex; align-items: center; gap: 7px; }
  .claims li.more { padding-left: 19px; font-style: italic; }
  .tick { width: 12px; height: 12px; flex: none; }
  .appointment { height: 85px; padding-top: 8px; }
  .appointment-title {
    font-size: 35px; font-weight: 700; line-height: 38px; letter-spacing: 0.5px;
  }
  .appointment-sub {
    font-size: 21px; font-style: italic; font-weight: 600; line-height: 26px;
  }
  .appointment-sub strong { font-style: normal; font-weight: 700; }
  .photo {
    height: 235px;
    background: radial-gradient(ellipse at 60% 40%, var(--photo-light) 0%, var(--photo-mid) 45%, var(--photo-dark) 100%);
  }
  .call { height: 82px; padding-top: 6px; }
  .call-title {
    font-size: 41px; font-weight: 700; line-height: 44px; letter-spacing: 0.5px;
    word-spacing: 6px;
  }
  .call-sub {
    font-size: 20px; font-style: italic; font-weight: 500; line-height: 24px; letter-spacing: 0.8px;
  }
  .footer {
    flex: 1;
    display: flex; align-items: center;
    padding: 0 20px;
    gap: 12px;
  }
  .brand { display: flex; align-items: center; gap: 6px; width: 48px; flex-direction: column; }
  .brand-mark { width: 16px; height: 16px; background: var(--ink-light); }
  .brand-name { font-size: 14px; font-weight: 600; }
  .firm-details { font-size: 14.5px; font-weight: 500; line-height: 19px; }
  .divider { margin: 0 8px; }
</style>
</head>
<body>
  <main class="flyer">
    <header class="band headline">WE FIGHT FOR YOU</header>

    <section class="intro">
      <p class="intro-text">If your own insurance company is refusing to pay what you are owed on a claim, call the Law Office of Dorvel K Tansy. <strong>We fight for you</strong> by examining the reasons your insurance carrier is denying or making an insufficient offer on the claim; updating and correcting claim documentation; making a new demand and filing a lawsuit if necessary. Whether it's a simple misunderstanding or something more complicated, <strong>WE CAN HELP!</strong></p>
      <p class="availability"><strong>OUR ATTORNEYS ARE AVAILABLE</strong> to help you cut through the nonsense.</p>
      <ul class="claims">
        <li><svg class="tick" viewBox="0 0 12 12"><path d="M1 6.5 L4.5 10 L11 1.5" fill="none" stroke="var(--tick)" stroke-width="2"/></svg>Hit and Run or Uninsured driver claims</li>
        <li><svg class="tick" viewBox="0 0 12 12"><path d="M1 6.5 L4.5 10 L11 1.5" fill="none" stroke="var(--tick)" stroke-width="2"/></svg>Catastrophic losses</li>
        <li><svg class="tick" viewBox="0 0 12 12"><path d="M1 6.5 L4.5 10 L11 1.5" fill="none" stroke="var(--tick)" stroke-width="2"/></svg>Fire, flood and property loss</li>
        <li><svg class="tick" viewBox="0 0 12 12"><path d="M1 6.5 L4.5 10 L11 1.5" fill="none" stroke="var(--tick)" stroke-width="2"/></svg>Business insurance</li>
        <li><svg class="tick" viewBox="0 0 12 12"><path d="M1 6.5 L4.5 10 L11 1.5" fill="none" stroke="var(--tick)" stroke-width="2"/></svg>Life insurance benefits</li>
        <li><svg class="tick" viewBox="0 0 12 12"><path d="M1 6.5 L4.5 10 L11 1.5" fill="none" stroke="var(--tick)" stroke-width="2"/></svg>Wrongful Death Benefits</li>
        <li><svg class="tick" viewBox="0 0 12 12"><path d="M1 6.5 L4.5 10 L11 1.5" fill="none" stroke="var(--tick)" stroke-width="2"/></svg>Health insurance claims</li>
        <li class="more">and many more</li>
      </ul>
    </section>

    <section class="band appointment">
      <p class="appointment-title">CALL TO MAKE AN APPOINTMENT</p>
      <p class="appointment-sub">for <strong>A FREE CONSULTATION</strong> with an attorney today!</p>
    </section>

    <div class="photo" role="img" aria-label="Photo of hands holding a smartphone and tapping the screen, light blue shirt sleeves"></div>

    <section class="band call">
      <p class="call-title">CALL US NOW! 602-574-2930</p>
      <p class="call-sub">We have mobile offices available to assist in your area.</p>
    </section>

    <footer class="footer">
      <div class="brand">
        <span class="brand-mark"></span>
        <span class="brand-name">Tansy</span>
      </div>
      <div class="firm-details">
        <p>Law Office of Dorvel K Tansy<span class="divider">|</span>4857 W 17th Avenue, Ste 406, Phoenix, AZ 85033</p>
        <p>www.tansylaw.com</p>
      </div>
    </footer>
  </main>
</body>
</html>
```